Web Design Project for Web Agency

WHAT I NEED:
The design I need (PSD file) is for a microsite designed for employee recruitment for Brantley, a Web agency.
***Design for the 1st Page ONLY : "Manifeste"
OBJECTIVES OF THE WEBSITE:
1. To promote the agency's corporate culture and HR management principles.
2. To get people to apply on available jobs
ELEMENTS OF THE PAGE "MANIFESTE" :
1. Brantley logo (see attached files). Beside the logo must be the word "Carrières" ("Careers" in english)
***The logo is not final and there is NO branding for Brantley yet. That is why there are multiple files. So please feel free to be creative!
2. Main menu : 4 sections
Manifeste | Opportunités | Brantly | Postuler
3. Manifeste :
This page is the home page. It will present 2 main sections :
a. The agency's corporate culture :
- Title of the page is a question : "Do you embrace Brantley's corporate culture?"
- Then, presentation of the 5 corporate values, each with a title and short description
- At the end of the list of values, we want a button that says "Apply now"
b. The agency's HR management principles :
- Title of the page is a question : "Do you see yourself working at Brantley?"
- Then, presentation of the 5 Management principles, each with a title and short description
- At the end of the list of principles, we want a button that says "Apply now"
VISUAL INSPIRATION
To create each section of the "Manifeste" page, we want a design that will fit with the corporate culture:
- Brantley is BOLD
- Brantley is PROUD
- Brantley is PROFESSIONAL
- Brantley is ELEGANT
- Brantley is REFINED
We want something slick and modern. Here are some Website's that we like that can be of inspiration:
- http://www.studio-vetrak.com/en/services
- http://quorvinpanels.com/

```html
<!DOCTYPE html>
<html lang="fr">
<head>
<meta charset="utf-8">
<title>Brantley — Carrières</title>
<link rel="stylesheet" href="https://fonts.googleapis.com/css2?family=Open+Sans:wght@400;600;700&display=swap">
<style>
:root{
  --ink:#1c1c1c;
  --nav:#151515;
  --accent:#ef6a2a;
  --text:#8a8a8a;
  --title:#222;
  --rule:#d6d6d6;
  --band:#2b2e33;
  --white:#fff;
}
*{box-sizing:border-box;margin:0;padding:0}
html,body{width:1200px;height:2776px;overflow:hidden;background:var(--white);font-family:"Open Sans",Arial,sans-serif;color:var(--text)}
.page{position:relative;width:1200px;height:2776px}

/* main menu */
.main-nav{position:absolute;top:0;left:0;width:1200px;height:62px;background:linear-gradient(#2c2c2c,var(--nav));display:flex}
.main-nav a{flex:1;display:flex;align-items:center;justify-content:center;color:var(--white);font-weight:700;font-size:19px;text-decoration:none;border-left:1px solid #3d3d3d}
.main-nav a.home{flex:0 0 148px;background:var(--white);color:var(--ink);border:0}

/* header */
.brand{position:absolute;top:98px;left:26px;display:flex;align-items:center;gap:16px}
.brand .mark{width:40px;height:40px;background:var(--accent)}
.brand .name{font-weight:600;font-size:46px;line-height:1;color:var(--title)}
.brand .section-label{font-size:22px;color:#666;padding-left:16px;border-left:1px solid var(--rule);line-height:40px}
.call{position:absolute;top:122px;right:24px;font-size:21px;color:#555}

/* hero */
.hero{position:absolute;top:200px;left:0;width:1200px;height:720px;background:radial-gradient(ellipse at 50% 30%,#6f6d69 0%,#3e3d3b 55%,#1f1f1f 100%)}
.hero h1{position:absolute;top:535px;left:0;width:100%;text-align:center;font-weight:400;font-size:54px;line-height:70px;color:var(--white);text-transform:uppercase}
.dots{position:absolute;top:950px;left:538px;display:flex;gap:10px}
.dots i{width:20px;height:20px;border-radius:50%;background:#ccc}
.dots i.on{background:#111}

/* sections */
.section-title{position:absolute;left:40px;font-size:24px;font-weight:600;color:var(--title);text-transform:uppercase}
.copy{position:absolute;left:40px;width:1120px;font-size:15px;line-height:26px}
.copy strong{color:var(--title);font-weight:600}
.rule{position:absolute;left:0;width:1200px;height:1px;background:var(--rule)}

/* columns */
.col{position:absolute;top:1370px}
.col h2{font-size:23px;font-weight:400;color:var(--title);text-transform:uppercase;text-align:center;white-space:nowrap;height:44px}
.col .icon{display:block;margin:38px auto 0;background:#1e1e1e;border-radius:6px;height:140px}
.col p{font-size:14px;line-height:24px;margin-top:42px}
.col p + p{margin-top:22px}
.col ul{list-style:none;margin-top:40px}
.col li{font-size:14px;line-height:20px;margin-bottom:8px;display:flex;align-items:center;gap:14px}
.col li b{color:var(--title);font-weight:600}
.col li svg{flex:none}
.btn{position:absolute;top:1850px;height:40px;padding:0 18px;border-radius:8px;background:linear-gradient(#444,#0e0e0e);color:var(--white);font-weight:700;font-size:16px;display:flex;align-items:center}

/* values */
.values{position:absolute;top:1992px;left:40px;width:1120px;display:flex;gap:24px}
.value{flex:1}
.value h3{font-size:16px;font-weight:600;color:var(--title);text-transform:uppercase;margin-bottom:6px}
.value p{font-size:14px;line-height:23px}

/* how we work */
.band{position:absolute;top:2190px;left:0;width:1200px;height:417px;background:linear-gradient(160deg,#4a4d52,var(--band) 55%,#1d1f22)}
.band h2{position:absolute;top:60px;width:100%;text-align:center;font-size:38px;font-weight:600;color:var(--white);text-transform:uppercase}
.band .play{position:absolute;top:140px;left:558px}
.band p{position:absolute;top:320px;left:120px;width:960px;text-align:center;font-size:20px;line-height:32px;font-weight:700;color:var(--white)}

/* footer */
.foot-links{position:absolute;top:2670px;left:40px;font-size:14px;font-weight:700;color:#444}
.foot-links span{color:#aaa;margin:0 6px}
.foot-bar{position:absolute;top:2712px;left:0;width:1200px;height:64px;background:linear-gradient(#2d2d2d,#0f0f0f);display:flex;align-items:center;justify-content:space-between;padding:0 40px}
.foot-bar small{font-size:14px;font-weight:700;color:var(--white)}
.social{display:flex;gap:10px}
.social i{width:34px;height:34px;background:#d9d9d9;border-radius:4px}
</style>
</head>
<body>
<div class="page">

<nav class="main-nav">
  <a class="home" href="#">Home</a>
  <a href="#">Manifeste</a>
  <a href="#">Opportunités</a>
  <a href="#">Brantly</a>
  <a href="#">Postuler</a>
  <a href="#">Contact Us</a>
</nav>

<header>
  <div class="brand">
    <span class="mark"></span>
    <span class="name">Brantley</span>
    <span class="section-label">Carrières</span>
  </div>
  <div class="call">Call Us: +91 555 014 2298</div>
</header>

<section class="hero" role="img" aria-label="Dark photograph of a hand writing with a pen">
  <h1>We create digital experiences for<br>brands and companies</h1>
</section>
<div class="dots"><i class="on"></i><i></i><i></i><i></i></div>

<h2 class="section-title" style="top:1008px">Welcome to Brantley</h2>
<p class="copy" style="top:1058px">Donec quam felis, ultricies nec, pellentesque eu, pretium quis, sem. Nulla consequat massa quis enim. Donec pede justo, fringilla vel, aliquet nec, vulputate eget, arcu. In enim justo, rhoncus ut, imperdiet a, venenatis vitae, justo. Nullam dictum felis eu pede mollis pretium. Donec quam felis, ultricies nec, pellentesque eu, pretium quis, sem. Nulla consequat massa quis enim. Donec pede justo, fringilla vel, aliquet nec, vulputate eget, arcu. In enim justo, rhoncus ut, imperdiet a, venenatis vitae, justo. Nullam dictum felis eu pede mollis pretium. Donec quam felis, ultricies nec, pellentesque eu, pretium quis, sem. Nulla consequat massa quis enim. Donec pede justo, fringilla vel, aliquet nec, vulputate eget, arcu. In enim justo, rhoncus ut, imperdiet a, venenatis vitae, justo. Nullam dictum felis eu pede mollis pretium.</p>
<p class="copy" style="top:1240px"><strong>Do you see yourself working at Brantley?</strong> Donec quam felis, ultricies nec, pellentesque eu, pretium quis, sem. Nulla consequat massa quis enim. Donec pede justo, fringilla vel, aliquet nec, vulputate eget, arcu. In enim justo, rhoncus ut, imperdiet a, venenatis vitae, justo. Nullam dictum felis eu pede.</p>

<div class="rule" style="top:1333px"></div>

<div class="col" style="left:40px;width:320px">
  <h2>Manifeste</h2>
  <div class="icon" role="img" aria-label="Pictogram of three people linked as a team" style="width:240px"></div>
  <p>Donec quam felis, ultricies nec, pellentesque eu, pretium quis, sem. Nulla consequat massa quis enim. Donec pede justo, fringilla vel, aliquet nec, vulputate eget, arcu.</p>
  <p>In enim justo, rhoncus ut, imperdiet a, venenatis vitae, justo. Nullam dictum felis eu pede mollis pretium.</p>
</div>
<div class="col" style="left:390px;width:380px">
  <h2>HR Management Principles</h2>
  <div class="icon" role="img" aria-label="Pictogram of a person beside a rising chart board" style="width:220px"></div>
  <ul>
    <li><svg width="14" height="14" viewBox="0 0 14 14"><path d="M2 1l11 6-11 6 3-6z" fill="#111"/></svg><span><b>Trust</b> — we give every talent room to lead.</span></li>
    <li><svg width="14" height="14" viewBox="0 0 14 14"><path d="M2 1l11 6-11 6 3-6z" fill="#111"/></svg><span><b>Growth</b> — training and mentoring all year.</span></li>
    <li><svg width="14" height="14" viewBox="0 0 14 14"><path d="M2 1l11 6-11 6 3-6z" fill="#111"/></svg><span><b>Openness</b> — clear goals, honest feedback.</span></li>
    <li><svg width="14" height="14" viewBox="0 0 14 14"><path d="M2 1l11 6-11 6 3-6z" fill="#111"/></svg><span><b>Balance</b> — flexible hours, real time off.</span></li>
    <li><svg width="14" height="14" viewBox="0 0 14 14"><path d="M2 1l11 6-11 6 3-6z" fill="#111"/></svg><span><b>Reward</b> — success shared with the team.</span></li>
  </ul>
</div>
<div class="col" style="left:800px;width:330px">
  <h2>Creative Ideas</h2>
  <div class="icon" role="img" aria-label="Pictogram of a person with a light bulb idea" style="width:120px"></div>
  <p>Donec quam felis, ultricies nec, pellentesque eu, pretium quis, sem. Nulla consequat massa quis enim. Donec pede justo, fringilla vel, aliquet nec, vulputate eget, arcu.</p>
  <p>In enim justo, rhoncus ut, imperdiet a, venenatis vitae, justo. Nullam dictum felis eu pede mollis pretium.</p>
</div>
<a class="btn" style="left:42px">Read More...</a>
<a class="btn" style="left:400px">Apply Now</a>
<a class="btn" style="left:802px">Read More...</a>

<div class="rule" style="top:1919px"></div>

<h2 class="section-title" style="top:1944px">Do you embrace Brantley's corporate culture?</h2>
<div class="values">
  <div class="value"><h3>Bold</h3><p>Donec quam felis, ultricies nec, pellentesque eu, pretium quis, sem. Nulla consequat massa quis enim.</p></div>
  <div class="value"><h3>Proud</h3><p>Donec pede justo, fringilla vel, aliquet nec, vulputate eget, arcu. In enim justo, rhoncus ut.</p></div>
  <div class="value"><h3>Professional</h3><p>Imperdiet a, venenatis vitae, justo. Nullam dictum felis eu pede mollis pretium quis sem.</p></div>
  <div class="value"><h3>Elegant</h3><p>Donec quam felis, ultricies nec, pellentesque eu, pretium quis. Nulla consequat massa enim.</p></div>
  <div class="value"><h3>Refined</h3><p>Fringilla vel, aliquet nec, vulputate eget, arcu. Nullam dictum felis eu pede mollis pretium.</p></div>
</div>

<section class="band" role="img" aria-label="Dim photograph of a fountain pen resting on a notebook">
  <h2>How we work</h2>
  <svg class="play" width="84" height="84" viewBox="0 0 84 84"><circle cx="42" cy="42" r="38" fill="#fff"/><circle cx="42" cy="42" r="30" fill="#1a1a1a"/><path d="M34 27l22 15-22 15z" fill="#fff"/></svg>
  <p>Donec quam felis, ultricies nec, pellentesque eu, pretium quis, sem. Nulla consequat massa quis enim. Donec pede justo, fringilla vel, aliquet nec, vulputate eget, arcu. Donec quam felis, ultricies nec.</p>
</section>

<footer>
  <div class="foot-links">Home<span>|</span>About Us<span>|</span>Manifeste<span>|</span>Opportunites<span>|</span>Brantly<span>|</span>Postuler<span>|</span>Contact Us</div>
  <div class="foot-bar">
    <small>Copyright © 2013 Brantley</small>
    <div class="social"><i></i><i></i><i></i><i></i><i></i></div>
  </div>
</footer>

</div>
</body>
</html>
```